Pella Acupuncture Business Card Design

I would like a business card design for my acupuncture business which is based from 2 practices in Melbourne, Australia.

The front of the card should include:

*The Logo
* Name - Miranda Tovelisca (B.App.Sc.(TCM), Dip.Rem.Mass.). (I would like the letters after my name in slightly smaller font)
* Mobile number - 0472 318 604
* Web address - www.pellaacupuncture-example.com.au

On the back of the card I would somehow like to fit my 2 clinic addresses in. They are:

The Birchwood Restoration Rooms
842 Fennimore Rd, Camberwell VIC 3124
Ph: 1300 274 518

Quillbrook Integrative & Eastern Herbal Therapy Clinic
31 Marlowby Rd, Malvern East VIC 3145
Ph: (03) 9871 3352

If there is space, I'd also like to add to the back of the card - Next Appointment............................ (or something along those lines).

Thanks and happy designing!

Target Market(s)

Health consumers, and colleagues in the health industry

Industry/Entity Type

Clinic

Contact Information for Business Card

as above in brief

Requirements
Must have
• I've seen some ok designs coming in, however I'd like to avoid the generic look with the added curved line details etc. I don't particularly need extra patterns added to the card. I'd prefer it to look quite clean and simple, and using more earthy colours (I'm not super keen on the lime green that a lot of designs seem to include. I don't mind the full black or white look, (obviously the back side needs to be a lighter colour to allow me to write appointment details on it). I also quite like the idea of the background looking like brown recycled paper (just an idea - that's not 100% necessary).
Nice to have
• I have an idea that I could have the main flower part of the logo printed as metallic.
Should not have
• Generic patterns and too much added detail.

```html
<!DOCTYPE html>
<html lang="en">
<head>
<meta charset="utf-8">
<title>Pella Acupuncture – Business Card</title>
<link rel="stylesheet" href="https://fonts.googleapis.com/css2?family=Open+Sans:wght@400;600;700&display=swap">
<style>
  :root {
    --backdrop: #3a322e;
    --card-black: #1c1c1c;
    --paper-white: #fbfbf9;
    --leaf-green: #7cbc2b;
    --sky-blue: #2a9fd4;
    --text-light: #d8d8d8;
    --text-muted: #b9b9b9;
    --ink-dark: #2b2b2b;
    --gold: #c99a2e;
    --cream: #f3efc0;
    --stripe: linear-gradient(90deg, var(--sky-blue) 0%, #8fd0c8 25%, var(--cream) 55%, #e4cf7a 75%, var(--gold) 100%);
    --stripe-rev: linear-gradient(90deg, var(--gold) 0%, #e4cf7a 25%, var(--cream) 50%, #8fd0c8 75%, var(--sky-blue) 100%);
  }
  * { box-sizing: border-box; margin: 0; padding: 0; }
  html, body { width: 1200px; height: 768px; overflow: hidden; }
  body {
    background: var(--backdrop);
    font-family: "Open Sans", Arial, sans-serif;
    display: flex;
    align-items: center;
    justify-content: center;
    gap: 40px;
  }
  .card {
    position: relative;
    width: 530px;
    height: 322px;
    background: var(--card-black);
    overflow: hidden;
    box-shadow: 0 8px 24px rgba(0,0,0,.45);
  }

  /* Front */
  .card-front .brand {
    position: absolute;
    left: 34px;
    top: 100px;
    width: 200px;
    display: flex;
    align-items: center;
    gap: 12px;
  }
  .brand-dot {
    width: 26px; height: 26px;
    border-radius: 50%;
    background: var(--gold);
    flex: none;
  }
  .brand-name {
    color: var(--leaf-green);
    font-weight: 600;
    font-size: 21px;
    line-height: 1.15;
  }
  .card-front .details {
    position: absolute;
    left: 250px;
    top: 108px;
    color: var(--text-light);
  }
  .person-name {
    color: var(--leaf-green);
    font-weight: 700;
    font-size: 17px;
  }
  .credentials {
    color: var(--text-muted);
    font-size: 10.5px;
    margin: 2px 0 12px;
  }
  .contact-list { list-style: none; }
  .contact-list li {
    display: flex;
    align-items: center;
    gap: 9px;
    font-size: 12.5px;
    line-height: 21px;
  }
  .contact-list svg { width: 11px; height: 11px; flex: none; fill: var(--sky-blue); }
  .front-stripe {
    position: absolute;
    left: 0; right: 0; bottom: 0;
    height: 7px;
    background: var(--stripe);
  }

  /* Back */
  .back-stripe {
    position: absolute;
    left: 0; right: 0;
    height: 7px;
  }
  .back-stripe.top { top: 0; background: var(--stripe-rev); }
  .back-stripe.bottom { bottom: 0; background: var(--stripe); }
  .clinics {
    position: absolute;
    left: 26px;
    top: 24px;
    right: 20px;
  }
  .clinics-title {
    color: var(--sky-blue);
    font-weight: 700;
    font-size: 11.5px;
    letter-spacing: .3px;
    margin-bottom: 3px;
  }
  .clinic { margin-bottom: 3px; }
  .clinic-name {
    color: var(--leaf-green);
    font-weight: 700;
    font-size: 12px;
    line-height: 16px;
  }
  .clinic-name::before { content: "»"; margin-right: 8px; }
  .clinic-address {
    color: var(--text-light);
    font-size: 11px;
    line-height: 15px;
    padding-left: 16px;
  }
  .appointment {
    position: absolute;
    left: 26px;
    right: 26px;
    top: 148px;
    height: 142px;
    background: var(--paper-white);
    padding: 16px 18px;
    color: var(--ink-dark);
    font-size: 12.5px;
  }
  .appointment-line {
    border-bottom: 1.5px dotted #555;
    height: 26px;
  }
  .appointment-line.first {
    display: flex;
    align-items: flex-end;
    border-bottom: none;
    height: 20px;
  }
  .appointment-line.first span { white-space: nowrap; }
  .appointment-line.first i {
    flex: 1;
    border-bottom: 1.5px dotted #555;
    margin-left: 2px;
    margin-bottom: 3px;
  }
</style>
</head>
<body>
  <section class="card card-front" aria-label="Card front">
    <div class="brand">
      <span class="brand-dot"></span>
      <span class="brand-name">Pella Acupuncture</span>
    </div>
    <div class="details">
      <p class="person-name">Miranda Tovelisca</p>
      <p class="credentials">B.App.Sc.(TCM), Dip.Rem.Mass.</p>
      <ul class="contact-list">
        <li>
          <svg viewBox="0 0 12 12" aria-hidden="true"><path d="M1 3.5C1 2 2.5 1 6 1s5 1 5 2.5v1H8.5V3.2H3.5v1.3H1zM2.5 6h7l1 5h-9z"/></svg>
          0472 318 604
        </li>
        <li>
          <svg viewBox="0 0 12 12" aria-hidden="true"><path d="M0 2h12v8H0zM1 3l5 3.5L11 3z" fill-rule="evenodd"/></svg>
          miranda@pellaacupuncture-example.com.au
        </li>
        <li>
          <svg viewBox="0 0 12 12" aria-hidden="true"><circle cx="6" cy="6" r="5.5"/></svg>
          www.pellaacupuncture-example.com.au
        </li>
      </ul>
    </div>
    <div class="front-stripe"></div>
  </section>

  <section class="card card-back" aria-label="Card back">
    <div class="back-stripe top"></div>
    <div class="clinics">
      <p class="clinics-title">CLINIC ADDRESSES</p>
      <div class="clinic">
        <p class="clinic-name">The Birchwood Restoration Rooms</p>
        <p class="clinic-address">842 Fennimore Rd, Camberwell VIC 3124 &nbsp;•&nbsp; Ph: 1300 274 518</p>
      </div>
      <div class="clinic">
        <p class="clinic-name">Quillbrook Integrative &amp; Eastern Herbal Therapy Clinic</p>
        <p class="clinic-address">31 Marlowby Rd, Malvern East VIC 3145 &nbsp;•&nbsp; Ph: (03) 9871 3352</p>
      </div>
    </div>
    <div class="appointment">
      <div class="appointment-line first"><span>Next Appointment</span><i></i></div>
      <div class="appointment-line"></div>
      <div class="appointment-line"></div>
      <div class="appointment-line"></div>
    </div>
    <div class="back-stripe bottom"></div>
  </section>
</body>
</html>
```